Make our white papers look like a must read

Our current white paper template doesn’t do our content justice. We want your help to make them look as good as the copy is.

Through our brivolt82 software, our company helps marketers to deliver more, better qualified leads and improved sales conversion through marketing automation, lead scoring and web analytics.

With this in mind, we are engaged in a content marketing programme which includes the distribution of a series of white-papers entitled “the Pocket Compass for…” So far the series consists of:

* The Pocket Compass For Marketing Automation
* The Pocket Compass For Email Marketing
* The Pocket Compass For Content Marketing

We are looking for a design that presents our content in the best format, looks great, is readable and communicates our core values - which are:

* Professional
* Innovative
* Approachable
* Transparent
* Straight talking
* Honest

We will be delivering our whitepapers online, through our website, so ultimately they will delivered as PDFs. However, it is anticipated that a significant number of users will prefer to print the whitepaper out and might want to scribble notes, so some white-space will be needed.

Our white papers normally consist of around 3,000 - 4,000 words and will be punctuated with bulleted lists, quote callouts, images (with and without captions) and graphs.

Summary of our Expectations
=======================
In-house, we use Adobe Indesign CS2 so it would be preferential if your submission was compatible with it.

For our stock images, we use lumagrove.

I've uploaded our current layout for information.

UK Based Digital Marketers of Small Medium Sized B2B companies.

Marketing

• Cover page
About Us/About the Author Page
Content Page
Section Break page
Content Page

```html
<!DOCTYPE html>
<html lang="en">
<head>
<meta charset="utf-8">
<title>The Pocket Compass for Marketing Automation – white paper pages</title>
<link rel="stylesheet" href="https://fonts.googleapis.com/css2?family=Bitter:wght@600;700&family=Quicksand:wght@400&family=Source+Sans+3:wght@400;600;700&display=swap">
<style>
  :root {
    --backdrop: #d9d9d6;
    --paper: #ffffff;
    --green: #8cc63f;
    --green-soft: #c9e39c;
    --ink: #2e2e2e;
    --text: #4a4a4a;
    --grey: #8a8a8a;
    --band: #ececec;
    --accent: #e2572b;
  }
  * { box-sizing: border-box; margin: 0; padding: 0; }
  html, body { width: 1200px; height: 1000px; overflow: hidden; }
  body { background: var(--backdrop); font-family: "Source Sans 3", Arial, sans-serif; color: var(--text); position: relative; }

  .page { position: absolute; top: 238px; width: 370px; height: 523px; background: var(--paper); box-shadow: 0 2px 10px rgba(0,0,0,.18); overflow: hidden; }
  .page--cover { left: 22px; }
  .page--author { left: 415px; }
  .page--defined { left: 808px; }

  /* cover */
  .brand { position: absolute; left: 34px; top: 34px; display: flex; align-items: center; gap: 5px; font-family: "Bitter", Georgia, serif; font-weight: 700; font-size: 14px; color: var(--green); }
  .brand__dot { width: 8px; height: 8px; border-radius: 50%; background: var(--green); }
  .cover__series { position: absolute; left: 34px; top: 56px; font-family: "Quicksand", Arial, sans-serif; font-size: 27px; color: #555; }
  .cover__art { position: absolute; left: 0; top: 100px; width: 370px; height: 330px; background: linear-gradient(160deg, #f2f2f2 0%, #dfeec4 55%, #a9d36a 100%); }
  .cover__spike { position: absolute; left: 0; top: 100px; }
  .cover__title { position: absolute; left: 0; right: 0; top: 452px; text-align: center; font-family: "Bitter", Georgia, serif; font-weight: 700; font-size: 25px; color: var(--ink); }

  /* inner pages */
  .page__band { position: absolute; left: 0; top: 0; width: 100%; height: 46px; background: linear-gradient(90deg, var(--band) 0%, #e3eed2 45%, var(--band) 100%); }
  .page__running { position: absolute; right: 12px; top: 8px; width: 62px; text-align: right; font-size: 6.5px; line-height: 1.15; font-weight: 700; color: var(--ink); }
  .page__spike { position: absolute; left: 0; top: 0; }
  .heading { font-family: "Bitter", Georgia, serif; font-weight: 700; color: var(--ink); }
  .body { font-size: 7.4px; line-height: 1.32; }

  .author__photo { position: absolute; left: 22px; top: 58px; width: 74px; height: 74px; border-radius: 50%; background: radial-gradient(circle at 50% 40%, #e9d2b8, #b79b7e); border: 2px solid #fff; box-shadow: 0 0 0 1px #ccc; }
  .author__bio { position: absolute; left: 104px; top: 56px; width: 150px; }
  .author__bio h2 { font-size: 10px; margin-bottom: 3px; }
  .author__more { position: absolute; left: 22px; top: 176px; width: 245px; }
  .author__more p + p { margin-top: 7px; }
  .audience { position: absolute; left: 22px; right: 22px; top: 328px; text-align: center; }
  .audience h2 { font-size: 10.5px; margin-bottom: 8px; }
  .audience p + p { margin-top: 7px; }

  .defined__tab { position: absolute; left: 12px; top: 30px; padding: 3px 10px; background: #fff; font-size: 9px; }
  .defined__dot { position: absolute; left: 160px; top: 38px; width: 6px; height: 6px; border-radius: 50%; background: var(--accent); }
  .defined__intro { position: absolute; left: 40px; right: 18px; top: 56px; text-align: right; }
  .defined__intro h2 { font-size: 9px; margin-bottom: 2px; }
  .defined__more { position: absolute; left: 16px; top: 122px; font-size: 9px; }
  .columns { position: absolute; left: 16px; right: 16px; top: 140px; display: grid; grid-template-columns: 1fr 1fr; gap: 14px; }
  .columns h3 { display: inline; font-family: "Bitter", Georgia, serif; font-size: 8.5px; color: var(--ink); }
  .columns p { margin-bottom: 7px; }
  .points { list-style: none; margin-bottom: 7px; }
  .points li { position: relative; padding-left: 10px; margin-bottom: 4px; }
  .points li::before { content: ""; position: absolute; left: 1px; top: 2.5px; border-left: 4px solid var(--green); border-top: 2.5px solid transparent; border-bottom: 2.5px solid transparent; }
</style>
</head>
<body>

<section class="page page--cover" aria-label="Cover">
  <div class="brand"><span class="brand__dot"></span>brivolt82</div>
  <div class="cover__series">Pocket Compass for</div>
  <div class="cover__art" role="img" aria-label="Illustration of interlocking green and grey gears with small figures and process arrows"></div>
  <svg class="cover__spike" width="370" height="330" viewBox="0 0 370 330" aria-hidden="true">
    <polygon points="236,330 300,330 352,18" fill="var(--green)"/>
  </svg>
  <h1 class="cover__title">Marketing Automation</h1>
</section>

<section class="page page--author" aria-label="About the author">
  <div class="page__band" role="img" aria-label="Faint header strip of gears and figures"></div>
  <div class="page__running">Pocket Compass for Marketing Automation</div>
  <svg class="page__spike" width="370" height="523" viewBox="0 0 370 523" aria-hidden="true">
    <polygon points="300,70 350,60 262,330" fill="var(--green)"/>
  </svg>
  <div class="author__photo" role="img" aria-label="Portrait photograph of the author"></div>
  <div class="author__bio body">
    <h2 class="heading">about the author</h2>
    <p>Clara Penwick is a Marketing Communications professional of 18 years. In her career Clara was on the board of a highly regarded integrated marketing agency and developed marketing communications strategies for brands such as Northwind Air, Hollis &amp; Crane, Postway, Lineteq and many more. In the last 4 years Clara became an independent consultant and is both a trainer in marketing and practitioner in marketing communication strategy.</p>
  </div>
  <div class="author__more body">
    <p>Clara trains her own clients and also works for the Guild of Direct and Digital Practice and The Academy of Marketing Practice. Her areas of expertise include Social Media Marketing, Digital Marketing, Content Marketing, Integrated Marketing and eCRM. Clara also works closely with clients and agencies to improve their relationships and working practices through the creation of agency management programmes.</p>
    <p><strong>@clarapenwick<br>profiles.example.net/clarapenwick</strong></p>
  </div>
  <div class="audience body">
    <h2 class="heading">who should read this guide?</h2>
    <p>Thank you for taking the time to download this Pocket Compass. We hope that it is both simple but informative.</p>
    <p>The fact that you have downloaded it probably means that the concept or term has hit your radar and you are rightly trying to understand the term and its implication better. You are most likely in a marketing role or have some connection to marketing and/or sales. But equally you could be in an IT or procurement department.</p>
  </div>
</section>

<section class="page page--defined" aria-label="What is marketing automation">
  <div class="page__band" role="img" aria-label="Faint header strip of gears and figures"></div>
  <div class="page__running">Pocket Compass for Marketing Automation</div>
  <div class="defined__tab heading">What is marketing automation</div>
  <div class="defined__dot"></div>
  <svg class="page__spike" width="370" height="523" viewBox="0 0 370 523" aria-hidden="true">
    <polygon points="205,60 250,52 215,420" fill="var(--green)" opacity=".55"/>
  </svg>
  <div class="defined__intro body">
    <h2 class="heading">marketing automation defined</h2>
    <p>Don't rely on the Openpedia description of marketing automation as it just doesn't go far enough. It says "a software platform designed for marketing departments to streamline high-touch, repetitive manual processes with automated solutions". This description is factually correct, but doesn't go nearly far enough.</p>
  </div>
  <div class="defined__more heading">but it's more than that...</div>
  <div class="columns body">
    <div>
      <p><h3>It is an 'enabler'</h3> – it makes marketing related communications with individual prospects or customers easier and more possible than ever before so that you can nurture individuals depending on their readiness to buy.</p>
      <p><h3>It is an 'engine'</h3> that allows you to process</p>
      <ul class="points">
        <li>behavioural data about an individual prospect's interactions with the majority of your digital assets across websites, landing pages, emails, social media, blogs etc</li>
        <li>provided data by the prospects themselves which is captured. Something that was a dream a few years ago or came at a huge price is now entirely feasible and cost effective for even a small business. You can now harness 'big data' and make meaningful decisions and design customer communications around it.</li>
      </ul>
    </div>
    <div>
      <p><h3>It's a tool</h3> that measures the effectiveness of your digital marketing efforts and reports in a powerful and insightful way in real time so you can make marketing decisions.</p>
      <p><h3>It automates</h3> previously manual tasks, in particular email, so that your marketing responds to the interactions of your prospects as soon as your prospect does something – rather than when you manually create a campaign that you then blast to a group of prospects.</p>
      <p>And what does this all lead to? – through the combination of all of its features, it enables a company to drive a stronger ROI from its marketing investment by</p>
      <ul class="points">
        <li>improving the quality of the marketing to individual prospects</li>
        <li>improving the marketing intelligence gleaned through carrying out activities which in turn enables you to improve performance</li>
        <li>to focus marketing budget on the things that make the most impact to your bottom line</li>
      </ul>
    </div>
  </div>
</section>

</body>
</html>
```